Need a sleek, professional business card design for a Web Development business

I need a unique business card designed for a web development company. It is also the parent company for any ventures I do, such as my ClipWave channel, startup ideas I have, etc. I am the single member of "Bright Harbor Code LLC." I will attach my basic logo here, so you will see the current color scheme and have the asset available. Thank you!

Target Market(s)

Startups, SMB's, Professionals

Industry/Entity Type

Business

Font styles to use
Other font styles liked:
• Lovello for headings is what I use, but not necessary.

Colors

Designer to choose colors to be used in the design.

Requirements
Nice to have
• Sleek is the word. Professional, modern, dark.
Should not have
• Any work from someone else's design. Lacking originality.

```html
<!DOCTYPE html>
<html lang="en">
<head>
<meta charset="utf-8">
<title>Bright Harbor Code LLC – Business Card</title>
<link rel="stylesheet" href="https://fonts.googleapis.com/css2?family=Josefin+Sans:wght@700&family=Open+Sans:wght@400&display=swap">
<style>
  :root {
    --page-bg: #ececec;
    --card-dark: #232323;
    --accent-top: #dc5f68;
    --accent-bottom: #e0914f;
    --accent-text: #e58a5e;
    --ink: #161616;
    --light-text: #e6e6e6;
  }
  * { margin: 0; padding: 0; box-sizing: border-box; }
  html, body {
    width: 1200px;
    height: 900px;
    overflow: hidden;
    background: var(--page-bg);
  }
  .sheet {
    width: 1200px;
    height: 900px;
    display: flex;
    align-items: center;
    justify-content: center;
    gap: 80px;
  }
  .card {
    width: 460px;
    height: 460px;
    border-radius: 44px;
    position: relative;
    display: flex;
    flex-direction: column;
    align-items: center;
    box-shadow: 0 10px 30px rgba(0,0,0,0.15);
  }
  .card--back {
    background: var(--card-dark);
    padding-top: 120px;
  }
  .card--front {
    background: linear-gradient(180deg, var(--accent-top), var(--accent-bottom));
    justify-content: center;
  }
  .brand {
    display: flex;
    flex-direction: column;
    align-items: center;
    gap: 18px;
  }
  .brand__dot {
    width: 58px;
    height: 58px;
    border-radius: 50%;
  }
  .card--back .brand__dot { background: var(--accent-text); }
  .card--front .brand__dot { background: var(--ink); width: 90px; height: 90px; }
  .brand__name {
    font-family: "Josefin Sans", sans-serif;
    font-weight: 700;
    text-transform: uppercase;
    letter-spacing: 1px;
    text-align: center;
  }
  .card--back .brand__name { color: var(--accent-text); font-size: 24px; }
  .card--front .brand__name { color: var(--ink); font-size: 30px; }
  .contact {
    margin-top: 44px;
    font-family: "Open Sans", sans-serif;
    font-size: 15px;
    color: var(--light-text);
    display: flex;
    flex-direction: column;
    align-items: center;
    gap: 14px;
  }
  .contact__row { display: flex; gap: 26px; }
  .contact__item { display: flex; align-items: center; gap: 8px; }
  .contact__icon { width: 16px; height: 16px; flex: none; }
</style>
</head>
<body>
<main class="sheet">
  <section class="card card--back" aria-label="Card back">
    <div class="brand">
      <span class="brand__dot"></span>
      <p class="brand__name">Bright Harbor Code LLC</p>
    </div>
    <div class="contact">
      <div class="contact__row">
        <span class="contact__item">
          <svg class="contact__icon" viewBox="0 0 16 16" aria-hidden="true">
            <path fill="#e0914f" d="M3 2h3l1 3-2 1.2a8 8 0 0 0 4.8 4.8L11 9l3 1v3a1 1 0 0 1-1 1A12 12 0 0 1 2 3a1 1 0 0 1 1-1z"/>
          </svg>
          000 000 0000
        </span>
        <span class="contact__item">
          <svg class="contact__icon" viewBox="0 0 16 16" aria-hidden="true">
            <rect x="1" y="3" width="14" height="10" rx="1.5" fill="#e0914f"/>
            <path d="M1.5 4 8 9l6.5-5" fill="none" stroke="#232323" stroke-width="1.4"/>
          </svg>
          hello@brightharborcode.com
        </span>
      </div>
      <span class="contact__item">
        <svg class="contact__icon" viewBox="0 0 16 16" aria-hidden="true">
          <rect x="2" y="2" width="12" height="12" rx="2" fill="#e0914f"/>
        </svg>
        /Bright Harbor Code
      </span>
    </div>
  </section>

  <section class="card card--front" aria-label="Card front">
    <div class="brand">
      <span class="brand__dot"></span>
      <p class="brand__name">Bright Harbor Code LLC</p>
    </div>
  </section>
</main>
</body>
</html>
```